Redesign Logo Business Cards and Stationary
Brivosa
Redesign Logo Business Cards and Stationary - Construction
Creative Brief
Construction Services Group
Yes
This logo will reflect our company's credibility as a proffesional in the Multi-Family Renovation Industry. http://www.brivosagroup.example/
Professional
Please keep the current color from our existing logo and web site. www.BrivosaGroup.example
Make sure you look at the current business card files attached and the business card examples attached to this project.
I will need cards as follows
Backside of card:
Our Services:
Interior Renovations
Exterior Painting & Carpentry
Concrete Work
Siding Installation
Step Tread Replacements
Front side:
Derek J. Whitcombe
President
Phone: 615-555-0182 Fax 866-555-0147
Email: Dwhitcombe@BrivosaGroup.example
1873-K Hollis Bend Rd. #529
Murfreesboro, TN 37190
www.BrivosaGroup.example
Rolf Tenneker
Vice-President
Phone: 404-555-0139 Fax 866-555-0147
Email: RTenneker@BrivosaGroup.example
Front:
Gideon Hulme
Administrative Manager
Phone: 615-555-0164 Fax 866-555-0147
Email: GHulme@BrivosaGroup.example
Oskar Dähn
Project Manager
Phone: 615-555-0121 Fax 866-555-0147
Email: ODahn@BrivosaGroup.example

```html
<!DOCTYPE html>
<html lang="en">
<head>
<meta charset="utf-8">
<title>Brivosa Business Card</title>
<link href="https://fonts.googleapis.com/css2?family=Roboto:wght@400;500;700;900&display=swap" rel="stylesheet">
<style>
  :root {
    --green: #8cc63f;
    --green-dark: #6fa52a;
    --charcoal: #3b3b3b;
    --text: #444444;
    --muted: #9a9a9a;
    --rule: #cfcfcf;
    --paper: #ffffff;
    --page: #ffffff;
  }
  * { margin: 0; padding: 0; box-sizing: border-box; }
  html, body { width: 1200px; height: 425px; overflow: hidden; background: var(--page); }
  body { font-family: "Roboto", Arial, sans-serif; color: var(--text); position: relative; }

  .card {
    position: absolute; top: 18px; width: 568px; height: 390px;
    background: var(--paper); overflow: hidden;
    box-shadow: 0 0 0 1px #e3e3e3;
  }
  .card--back { left: 18px; }
  .card--front { left: 614px; }

  .stripes { position: absolute; left: 0; top: 0; width: 568px; height: 390px; }

  .band {
    position: absolute; left: 0; bottom: 0; width: 100%; height: 70px;
    background: var(--charcoal);
  }
  .band__phone {
    position: absolute; top: 50%; transform: translateY(-50%);
    display: flex; align-items: center; gap: 14px;
    color: #fff; font-weight: 700; font-size: 31px; letter-spacing: 0.3px;
  }
  .phone-badge {
    width: 40px; height: 40px; border-radius: 50%; background: var(--green);
    border: 3px solid #fff; display: flex; align-items: center; justify-content: center;
  }

  /* Back side */
  .services-title {
    position: absolute; left: 32px; top: 26px; font-size: 25px; font-weight: 500; color: var(--text);
  }
  .services-title span { color: var(--green); font-weight: 700; }
  .services-list { position: absolute; left: 38px; top: 142px; list-style: none; }
  .services-list li {
    font-size: 19px; line-height: 27px; color: var(--text); position: relative; padding-left: 20px;
  }
  .services-list li::before {
    content: ""; position: absolute; left: 0; top: 8px;
    border-left: 9px solid var(--green); border-top: 6px solid transparent; border-bottom: 6px solid transparent;
  }

  .brand {
    position: absolute; display: flex; flex-direction: column; align-items: center; gap: 10px;
  }
  .brand__mark { width: 84px; height: 84px; background: var(--green); }
  .brand__name { font-size: 46px; font-weight: 900; color: var(--charcoal); letter-spacing: 1px; line-height: 1; }
  .card--back .brand { left: 318px; top: 116px; }
  .card--front .brand { left: 34px; top: 116px; }

  /* Front side */
  .person { position: absolute; right: 26px; top: 26px; text-align: right; }
  .person__name { font-size: 23px; font-weight: 700; color: var(--charcoal); }
  .person__title { font-size: 14px; color: var(--green); margin-top: 2px; }

  .contact {
    position: absolute; left: 290px; right: 26px; top: 138px;
    font-size: 13px; color: var(--text);
  }
  .contact__row { display: flex; align-items: center; gap: 8px; height: 22px; white-space: nowrap; }
  .contact__icon { width: 12px; height: 12px; border-radius: 2px; background: var(--green); flex: none; }
  .contact__address { margin-top: 10px; line-height: 20px; }

  .card--back .band__phone { left: 178px; }
  .card--front .band__phone { left: 34px; }
  .band__tagline {
    position: absolute; right: 22px; top: 50%; transform: translateY(-50%);
    color: #fff; font-size: 12px; line-height: 16px; text-align: left;
  }
</style>
</head>
<body>

<section class="card card--back">
  <svg class="stripes" viewBox="0 0 568 390" aria-hidden="true">
    <path d="M0 88 H330 L372 66 H568" fill="none" stroke="var(--green)" stroke-width="7"/>
    <path d="M0 99 H336 L378 77 H568" fill="none" stroke="var(--green)" stroke-width="2"/>
    <path d="M0 106 H340 L382 84 H568" fill="none" stroke="var(--rule)" stroke-width="2"/>
    <path d="M0 290 H210 L246 306 H568" fill="none" stroke="var(--rule)" stroke-width="2"/>
    <path d="M0 297 H206 L242 313 H568" fill="none" stroke="var(--green)" stroke-width="2"/>
    <path d="M0 308 H200 L236 322 H568" fill="none" stroke="var(--green)" stroke-width="7"/>
  </svg>

  <h2 class="services-title"><span>Our</span>Services:</h2>
  <ul class="services-list">
    <li>Interior Renovations</li>
    <li>Exterior Painting &amp; Carpentry</li>
    <li>Concrete Work</li>
    <li>Siding Installation</li>
    <li>Step Tread Replacements</li>
  </ul>

  <div class="brand">
    <div class="brand__mark"></div>
    <div class="brand__name">BRIVOSA</div>
  </div>

  <div class="band">
    <div class="band__phone">
      <span class="phone-badge">
        <svg width="20" height="20" viewBox="0 0 24 24" aria-hidden="true"><path fill="#fff" d="M6.6 10.8a15.1 15.1 0 0 0 6.6 6.6l2.2-2.2c.3-.3.7-.4 1-.2 1.1.4 2.3.6 3.6.6.6 0 1 .4 1 1V20c0 .6-.4 1-1 1A17 17 0 0 1 3 4c0-.6.4-1 1-1h3.5c.6 0 1 .4 1 1 0 1.3.2 2.5.6 3.6.1.3 0 .7-.2 1z"/></svg>
      </span>
      615-555-0182
    </div>
  </div>
</section>

<section class="card card--front">
  <svg class="stripes" viewBox="0 0 568 390" aria-hidden="true">
    <path d="M0 84 H260 L300 102 H568" fill="none" stroke="var(--green)" stroke-width="7"/>
    <path d="M0 95 H256 L296 113 H568" fill="none" stroke="var(--green)" stroke-width="2"/>
    <path d="M0 102 H252 L292 120 H568" fill="none" stroke="var(--rule)" stroke-width="2"/>
    <path d="M0 290 H330 L366 306 H568" fill="none" stroke="var(--rule)" stroke-width="2"/>
    <path d="M0 297 H326 L362 313 H568" fill="none" stroke="var(--green)" stroke-width="2"/>
    <path d="M0 308 H320 L356 322 H568" fill="none" stroke="var(--green)" stroke-width="7"/>
  </svg>

  <div class="person">
    <div class="person__name">Derek J. Whitcombe</div>
    <div class="person__title">President</div>
  </div>

  <div class="brand">
    <div class="brand__mark"></div>
    <div class="brand__name">BRIVOSA</div>
  </div>

  <div class="contact">
    <div class="contact__row"><span class="contact__icon"></span>866-555-0147</div>
    <div class="contact__row"><span class="contact__icon"></span>Dwhitcombe@BrivosaGroup.example</div>
    <div class="contact__row"><span class="contact__icon"></span>www.BrivosaGroup.example</div>
    <div class="contact__address">1873-K Hollis Bend Rd. #529<br>Murfreesboro,<br>TN 37190</div>
  </div>

  <div class="band">
    <div class="band__phone">
      <span class="phone-badge">
        <svg width="20" height="20" viewBox="0 0 24 24" aria-hidden="true"><path fill="#fff" d="M6.6 10.8a15.1 15.1 0 0 0 6.6 6.6l2.2-2.2c.3-.3.7-.4 1-.2 1.1.4 2.3.6 3.6.6.6 0 1 .4 1 1V20c0 .6-.4 1-1 1A17 17 0 0 1 3 4c0-.6.4-1 1-1h3.5c.6 0 1 .4 1 1 0 1.3.2 2.5.6 3.6.1.3 0 .7-.2 1z"/></svg>
      </span>
      615-555-0182
    </div>
    <div class="band__tagline">Multi-Family Exterior &amp; Interior<br>Renovation Contractors</div>
  </div>
</section>

</body>
</html>
```